Tallpine Company Flyer - RV Solar and Residential Solar

We would like to create a tri-fold brochure for our company for distribution in the mail. This will advertise our services, products and some references.

Our cover page should include a logo and contact information as well as some solar stock imagery.

Our inside pages should cover residential solar, RV solar and a solar education / facts portion.

The rear pages would be left for our remaining services and some references / testimonials.

Target Market(s)

Residential Homeowners and Recreational Vehicles

Industry/Entity Type

Solar Energy

Font styles to use
Serif
Sans Serif

Requirements
Must have
• Must match the color scheme of our logo.
Nice to have
• Solar stock images for RV solar and residential solar.
Either a black or white background with our logo is eye-catching,

```html
<!DOCTYPE html>
<html lang="en">
<head>
<meta charset="utf-8">
<title>Tallpine Renewables – Tri-fold Brochure Outside</title>
<link href="https://fonts.googleapis.com/css2?family=Raleway:wght@500;700;800&family=Open+Sans:ital,wght@0,400;0,600;1,400&family=Libre+Baskerville:wght@700&family=Oswald:wght@500&display=swap" rel="stylesheet">
<style>
  :root{
    --navy:#3a4fa3;
    --navy-deep:#2f4195;
    --green:#5bb531;
    --green-dark:#4a9e2a;
    --sky:#38b6e4;
    --ink:#3a3a3a;
    --paper:#f6f6f6;
    --stage:#3c3c3c;
    --quote-red:#d8506a;
  }
  *{box-sizing:border-box;margin:0;padding:0}
  html,body{width:828px;height:1200px;overflow:hidden;background:var(--stage)}
  body{position:relative;font-family:"Open Sans",sans-serif;color:var(--ink)}
  .brochure{position:absolute;left:14px;top:317px;width:800px;height:566px;background:var(--paper);overflow:hidden;box-shadow:0 6px 24px rgba(0,0,0,.45)}
  .brochure-art{position:absolute;inset:0}
  .abs{position:absolute}
  .panel-title{font-family:"Raleway",sans-serif;font-weight:800;line-height:1.15}
  .green{color:var(--green)}
  .navy{color:var(--navy)}

  /* left panel */
  .facts-head{left:22px;top:18px;display:flex;gap:8px;align-items:flex-start}
  .brand-dot{width:14px;height:14px;border-radius:50%;background:var(--sky);margin-top:6px}
  .facts-head .panel-title{font-size:13px}
  .facts-rule{left:56px;top:54px;width:70px;height:2px;background:var(--navy)}
  .facts-list{left:22px;top:64px;width:232px;list-style:none;font-size:7.4px;line-height:1.35}
  .facts-list li{position:relative;padding-left:13px;margin-bottom:3.4px}
  .facts-list li::before{content:"";position:absolute;left:1px;top:3px;width:3.5px;height:3.5px;border-radius:50%;background:var(--navy)}
  .relocate{left:10px;top:463px;width:247px;text-align:center}
  .relocate .panel-title{font-size:12.5px}
  .relocate p{color:#fff;font-size:12.5px;line-height:1.25;margin-top:2px;font-family:"Raleway",sans-serif;font-weight:500}

  /* middle panel */
  .project-head{left:272px;top:18px;width:258px;text-align:center;font-size:15px}
  .project-rule{left:373px;top:98px;width:56px;height:2px;background:var(--navy)}
  .services{left:277px;top:114px;width:248px;text-align:center}
  .services h3{font-family:"Raleway",sans-serif;font-weight:800;font-size:8.5px;color:var(--green)}
  .services p{font-size:8.8px;line-height:1.4;margin-top:1px}
  .quote-mark{left:375px;top:180px;font-family:"Libre Baskerville",serif;font-size:44px;line-height:1;color:var(--green)}
  .testimonial{left:300px;top:206px;width:196px;text-align:center;font-size:6.2px;font-style:italic;line-height:1.6;color:#444}
  .client-name{left:300px;top:287px;width:196px;text-align:center;font-family:"Raleway",sans-serif;font-weight:700;font-size:9.5px;color:var(--navy)}
  .contact{left:284px;top:452px;color:#fff}
  .contact h3{font-family:"Raleway",sans-serif;font-weight:800;font-size:12.5px}
  .contact h3 span{color:#fff}
  .contact-icons{display:flex;gap:6px;margin:6px 0 5px}
  .contact-icons i{width:12px;height:12px;border-radius:50%;background:var(--sky);display:block}
  .contact p{font-size:7px;line-height:1.5}
  .follow{left:436px;top:492px;color:#fff;font-size:7px;text-align:center}
  .follow-dots{display:flex;gap:6px;margin-top:6px}
  .follow-dots i{width:14px;height:14px;border-radius:50%;background:#fff;display:block}

  /* right panel */
  .brand{left:640px;top:96px;width:150px;text-align:center}
  .brand-mark{width:26px;height:26px;border-radius:50%;background:var(--sky);margin:0 auto 6px}
  .brand-name{font-family:"Raleway",sans-serif;font-weight:800;font-size:21px;color:var(--navy);letter-spacing:.5px;line-height:1}
  .brand-sub{font-family:"Raleway",sans-serif;font-weight:800;font-size:8px;color:var(--navy);letter-spacing:1.5px;margin-top:3px}
  .badge{left:700px;top:343px;width:76px;height:76px;border-radius:50%;background:#fff;border:4px solid var(--green);display:flex;flex-direction:column;align-items:center;justify-content:center;font-family:"Oswald",sans-serif;font-weight:500;line-height:1.02;color:var(--green);font-size:11px;text-align:center}
  .badge b{display:block;margin-top:2px;background:#222;color:#fff;font-weight:500;font-size:8px;padding:1px 4px}
  .welcome{left:560px;top:432px;width:240px;text-align:center}
  .welcome small{display:block;font-family:"Raleway",sans-serif;font-weight:500;font-size:11px;letter-spacing:4px;color:var(--green)}
  .welcome h2{font-family:"Libre Baskerville",serif;font-weight:700;font-size:22px;line-height:1.1;color:#fff;margin-top:3px}
  .quote-cta{left:618px;top:518px;width:140px;text-align:center;font-family:"Raleway",sans-serif;font-weight:800;font-size:11px;color:var(--navy)}
  .phones{left:534px;top:541px;width:266px;text-align:center;font-family:"Raleway",sans-serif;font-weight:800;font-size:11.5px;color:#fff}
  .phones span{font-weight:500}

  .footer-text{top:544px;width:266px;text-align:center;color:#fff;font-size:7.6px;letter-spacing:1px}
</style>
</head>
<body>
<main class="brochure">
  <svg class="brochure-art" width="800" height="566" viewBox="0 0 800 566" aria-hidden="true">
    <defs>
      <linearGradient id="skyFill" x1="0" y1="0" x2="0" y2="1">
        <stop offset="0" stop-color="#dfe9f3"/>
        <stop offset=".5" stop-color="#f0ede6"/>
        <stop offset=".75" stop-color="#c98a4e"/>
        <stop offset="1" stop-color="#6f7a3c"/>
      </linearGradient>
      <radialGradient id="bulbFill" cx=".5" cy=".45" r=".6">
        <stop offset="0" stop-color="#e8ec6a"/>
        <stop offset=".5" stop-color="#7cb53a"/>
        <stop offset="1" stop-color="#2f5a22"/>
      </radialGradient>
      <radialGradient id="houseFill" cx=".5" cy=".4" r=".7">
        <stop offset="0" stop-color="#e6f4ee"/>
        <stop offset=".6" stop-color="#8fc2a4"/>
        <stop offset="1" stop-color="#2f6e55"/>
      </radialGradient>
    </defs>
    <!-- panel paper -->
    <rect x="267" y="0" width="267" height="566" fill="#fafafa"/>
    <!-- cover photo -->
    <rect x="534" y="0" width="266" height="440" fill="url(#skyFill)" role="img" aria-label="Sky above a field of solar panels at sunset"/>
    <!-- brand plate behind logo -->
    <path d="M610 0 H800 V250 C740 230 690 220 640 200 Z" fill="#f7f8fa" opacity=".85"/>
    <!-- navy wave across the bottom -->
    <path d="M0 342 C60 330 140 340 230 350 C330 360 420 365 510 375 C580 385 640 365 700 350 C740 340 780 330 800 320 V566 H0 Z" fill="var(--navy)"/>
    <path d="M0 342 C60 330 140 340 230 350 C300 357 340 360 380 362" stroke="var(--green)" stroke-width="3" fill="none"/>
    <!-- badge stripe -->
    <rect x="740" y="360" width="60" height="40" fill="var(--sky)"/>
    <!-- photo circles -->
    <circle cx="133" cy="358" r="72" fill="var(--green)"/>
    <circle cx="133" cy="358" r="64" fill="url(#bulbFill)" role="img" aria-label="Glowing light bulb with a globe among green leaves"/>
    <circle cx="347" cy="398" r="56" fill="var(--green)"/>
    <circle cx="347" cy="398" r="49" fill="url(#houseFill)" role="img" aria-label="Wireframe house rising from a tablet on green grass"/>
    <!-- testimonial frame -->
    <rect x="290" y="203" width="216" height="80" rx="10" fill="none" stroke="var(--quote-red)" stroke-width=".8" stroke-dasharray="3 2"/>
    <rect x="365" y="195" width="66" height="14" fill="#fafafa"/>
    <rect x="335" y="280" width="126" height="8" fill="#fafafa"/>
    <!-- quote tab -->
    <path d="M628 537 L634 515 Q636 510 642 510 H744 Q750 510 752 515 L758 537 Z" fill="#fff"/>
    <!-- footer bands -->
    <rect x="0" y="537" width="267" height="29" fill="var(--green-dark)"/>
    <rect x="267" y="537" width="267" height="29" fill="var(--sky)"/>
    <rect x="534" y="537" width="266" height="29" fill="var(--green-dark)"/>
  </svg>

  <!-- left panel: solar facts -->
  <header class="abs facts-head">
    <span class="brand-dot"></span>
    <h2 class="panel-title"><span class="green">SOLAR 101</span><br><span class="navy">SOME FACTS ON SOLAR</span></h2>
  </header>
  <div class="abs facts-rule"></div>
  <ul class="abs facts-list">
    <li>Alberta is the sunniest province in Canada and comparable to Florida</li>
    <li>Systems are designed to last 25 years but operate for as long as 40 years</li>
    <li>Virtually no maintenance required!</li>
    <li>How your power bill works.</li>
    <li>Protect yourself from rising power costs</li>
    <li>Not everyone can have solar. Once 30-40% of the market has solar, utilities will not allow all solar systems to be installed.</li>
    <li>Dispel the snow myth: Snow only reduces a systems output by 5-8% over the course of a year. This is because our sunny hours are mostly made up in the longer summer days.</li>
    <li>Solar panels are nearly indestructible. Hail cannot damage a solar panel.</li>
    <li>Any extra power generated in the summer is sold back to the grid as a credit on your bill.</li>
  </ul>
  <div class="abs relocate">
    <h3 class="panel-title green">SELLING YOUR HOUSE AND<br>LOVE YOUR SOLAR?</h3>
    <p>We will relocate the system to<br>your new home for a small fee.</p>
  </div>
  <p class="abs footer-text" style="left:0">Sales@Tallpinerenewables.com</p>

  <!-- middle panel: services & testimonial -->
  <h2 class="abs panel-title project-head"><span class="green">A GREAT PLACE TO<br>START YOUR</span><br><span class="navy">RENEWABLE ENERGY<br>PROJECT!</span></h2>
  <div class="abs project-rule"></div>
  <section class="abs services">
    <h3>OTHER SERVICES OFFERED</h3>
    <p>Agricultural pivot power, oil and gas systems, energy audits, battery storage systems, off grid designs for cottages / lake houses</p>
  </section>
  <div class="abs quote-mark">&ldquo;</div>
  <blockquote class="abs testimonial">Lorem Ipsum is simply dummy text of the printing and typesetting industry. Lorem Ipsum has been the industry's standard dummy text ever since the 1500s, when an unknown printer took a galley of type and scrambled it to make a type specimen book.</blockquote>
  <p class="abs client-name">Client Name</p>
  <section class="abs contact">
    <h3 class="green">GET IN <span>TOUCH</span></h3>
    <div class="contact-icons"><i></i><i></i><i></i></div>
    <p>Ridgeway Valley, Alberta, Canada<br>555.310.6466<br>555.201.4605<br>sales@tallpinerenewables.com</p>
  </section>
  <div class="abs follow">Follow Us<div class="follow-dots"><i></i><i></i><i></i></div></div>
  <p class="abs footer-text" style="left:267px">www.tallpinerenewables.com</p>

  <!-- right panel: cover -->
  <div class="abs brand">
    <div class="brand-mark"></div>
    <div class="brand-name">TALLPINE</div>
    <div class="brand-sub">RENEWABLES</div>
  </div>
  <div class="abs badge">LOWEST<br>INSTALLED<br>SOLAR PRICE<b>GUARANTEED</b></div>
  <div class="abs welcome">
    <small>WELCOME TO</small>
    <h2>TALLPINE<br>RENEWABLES</h2>
  </div>
  <p class="abs quote-cta">Get a Free Quotation</p>
  <p class="abs phones">555-201-4605 <span>or</span> 555-310-6466</p>
</main>
</body>
</html>
```